Letterhead Design Project

We have recently updated our corporate logo and are seeking a new letterhead template.

Attached is the new logo and the old letterhead.

PLEASE DO NOT USE OUR EXISTING WEB SITE FOR INSPIRATION as we are redesigning it.

Target Market(s)

Executives, search professionals, technical and scientific professionals

Industry/Entity Type

Seeking

```html
<!DOCTYPE html>
<html lang="en">
<head>
<meta charset="utf-8">
<title>HelixPath Letterhead</title>
<link rel="stylesheet" href="https://fonts.googleapis.com/css2?family=Arimo:wght@400;700&family=Tinos&display=swap">
<style>
  :root {
    --paper: #ffffff;
    --ink: #333333;
    --brand-dark: #4d5a5c;
    --brand-blue: #1a9ad6;
    --ornament-grey: #9a9a9a;
    --ornament-blue: #4a90b2;
    --footer-grey: #5a5a5a;
    --footer-blue: #3399c4;
    --footer-ink: #111111;
  }
  html, body {
    margin: 0;
    padding: 0;
    overflow: hidden;
    background: var(--paper);
  }
  .letterhead {
    position: relative;
    width: 816px;
    height: 1200px;
    background: var(--paper);
    overflow: hidden;
  }
  .corner-ornament {
    position: absolute;
    left: 0;
    top: 0;
    width: 156px;
    height: 156px;
    background: linear-gradient(160deg, var(--ornament-grey) 0%, var(--ornament-blue) 55%, var(--ornament-blue) 100%);
  }
  .brand {
    position: absolute;
    left: 203px;
    top: 26px;
    display: flex;
    align-items: center;
    gap: 10px;
  }
  .brand-dot {
    width: 46px;
    height: 46px;
    border-radius: 50%;
    background: var(--brand-blue);
  }
  .brand-name {
    font-family: "Arimo", Arial, sans-serif;
    font-weight: 700;
    font-size: 42px;
    letter-spacing: -0.5px;
    color: var(--brand-dark);
  }
  .address {
    position: absolute;
    left: 277px;
    top: 102px;
    margin: 0;
    font-family: "Arimo", Arial, sans-serif;
    font-style: normal;
    font-size: 18px;
    line-height: 23px;
    color: var(--ink);
  }
  .footer-contacts {
    position: absolute;
    left: 0;
    top: 1088px;
    width: 816px;
    height: 72px;
    background: var(--footer-grey);
    box-shadow: 0 -2px 4px rgba(0,0,0,0.35);
    font-family: "Tinos", "Times New Roman", serif;
    font-size: 20px;
    line-height: 27px;
    color: var(--brand-blue);
  }
  .phone-lines {
    position: absolute;
    left: 20px;
    top: 11px;
  }
  .phone-lines .label {
    display: inline-block;
    width: 76px;
  }
  .email-lines {
    position: absolute;
    right: 20px;
    top: 11px;
    text-align: center;
  }
  .footer-web {
    position: absolute;
    left: 0;
    top: 1160px;
    width: 816px;
    height: 40px;
    background: var(--footer-blue);
    font-family: "Tinos", "Times New Roman", serif;
    font-size: 22px;
    line-height: 40px;
    letter-spacing: 1px;
    text-align: center;
    color: var(--footer-ink);
  }
</style>
</head>
<body>
<div class="letterhead">
  <div class="corner-ornament" role="img" aria-label="Decorative grey and blue folded ribbon arrow pointing down-right"></div>

  <div class="brand">
    <span class="brand-dot"></span>
    <span class="brand-name">HelixPath</span>
  </div>

  <address class="address">
    2400 Harbor View Road, Suite 140<br>
    Northfield, MA 01360
  </address>

  <footer>
    <div class="footer-contacts">
      <div class="phone-lines">
        <div><span class="label">Phone:</span>+1.555.014.0100</div>
        <div><span class="label">Fax:</span>+1.555.014.0110</div>
      </div>
      <div class="email-lines">
        <div>Contact Email:</div>
        <div>contact-us@helixpath.com</div>
      </div>
    </div>
    <div class="footer-web">www.helixpath.com</div>
  </footer>
</div>
</body>
</html>
```